Business Card Design Project

We need a business card designed for a new Luxury Custom Homebuilding company based in Arizona. We previous were called "Belcrest Estates" but want to start using "Belcrest Custom Homes" We want the message to communicate high end, luxury and cutting-edge. We like the blue, white and black color scheme.
Belcrest Custom Homes
Marcus T. Halloway
Chief Executive Officer
Office: 480-555-0142
Mobile: 480-555-0178
email: marc@belcrestcustom-example.com
web adress: www.BelcrestCustom-example.com
Updates
We have made a change to our website address and email address based on recieving feedback from a nmber of individuals. The feedback was web address and email address was to long. Therefore we have made a change. The new web adress and email adress are the following.
www.BelcrestCustom-example.com
marc@belcrestcustom-example.com
Also I decided against using in yellow. I like the colors blue,black, white and maybe gray.
Target Market(s)
Our target market is the wealthy individuals looking for a luxury high-end custom home.
Industry/Entity Type
Business
Look and feel

```html
<!DOCTYPE html>
<html lang="en">
<head>
<meta charset="utf-8">
<title>Belcrest Custom Homes – Business Card</title>
<link rel="stylesheet" href="https://fonts.googleapis.com/css2?family=Mulish:wght@700;800&family=Questrial&family=Roboto+Condensed:wght@400;700&display=swap">
<style>
  :root {
    --page: #ffffff;
    --card: #000000;
    --card-edge: #3a3a3a;
    --white: #ffffff;
    --blue: #4f86d4;
    --gray: #c4c7cc;
    --label: #333333;
  }
  html, body {
    margin: 0;
    padding: 0;
    overflow: hidden;
  }
  body {
    width: 1180px;
    height: 1200px;
    background: var(--page);
    position: relative;
  }
  .side-label {
    position: absolute;
    left: 0;
    font-family: Arial, Helvetica, sans-serif;
    font-weight: 700;
    font-size: 22px;
    color: var(--label);
    text-decoration: underline;
    letter-spacing: 1.2px;
  }
  .side-label--front { top: 525px; }
  .side-label--back { top: 661px; }
  .card {
    position: absolute;
    left: 150px;
    width: 1028px;
    background: var(--card);
    border: 1px solid var(--card-edge);
    color: var(--white);
    text-align: center;
  }
  .card--front { top: 0; height: 587px; }
  .card--back { top: 610px; height: 588px; }
  .brand-name {
    position: absolute;
    top: 122px;
    left: 0;
    right: 0;
    margin: 0;
    font-family: "Roboto Condensed", "Arial Narrow", sans-serif;
    font-weight: 700;
    font-size: 62px;
    letter-spacing: -0.5px;
    color: var(--white);
  }
  .person {
    position: absolute;
    top: 321px;
    left: 0;
    right: 0;
    font-family: Mulish, "Century Gothic", sans-serif;
  }
  .person__name {
    margin: 0;
    font-weight: 800;
    font-size: 35px;
    color: var(--white);
    text-decoration: underline;
    text-underline-offset: 4px;
    text-decoration-thickness: 2px;
    line-height: 1.2;
  }
  .person__title {
    margin: 2px 0 0;
    font-weight: 800;
    font-size: 30px;
    color: var(--blue);
    line-height: 1.2;
  }
  .contact {
    position: absolute;
    top: 476px;
    left: 0;
    right: 0;
    margin: 0;
    font-family: Questrial, "Century Gothic", sans-serif;
    font-size: 24px;
    line-height: 29.5px;
    color: var(--gray);
  }
  .contact p { margin: 0; }
  .web-address {
    position: absolute;
    top: 241px;
    left: 0;
    right: 0;
    margin: 0;
    font-family: "Roboto Condensed", "Arial Narrow", sans-serif;
    font-size: 52px;
    letter-spacing: -0.5px;
    color: var(--white);
  }
  .web-address__name { font-weight: 700; }
  .web-address__name--blue { color: var(--blue); }
</style>
</head>
<body>
  <span class="side-label side-label--front">FRONT SIDE</span>
  <section class="card card--front" aria-label="Business card front">
    <h1 class="brand-name">Belcrest Custom Homes</h1>
    <div class="person">
      <p class="person__name">Marcus T. Halloway</p>
      <p class="person__title">Chief Executive Officer</p>
    </div>
    <div class="contact">
      <p>Office: (480) 555-0142</p>
      <p>Mobile: (480) 555-0178</p>
      <p>Email: marc@belcrestcustom-example.com</p>
    </div>
  </section>

  <span class="side-label side-label--back">BACK SIDE</span>
  <section class="card card--back" aria-label="Business card back">
    <p class="web-address">www.<span class="web-address__name">Belcrest</span><span class="web-address__name web-address__name--blue">Custom-example</span>.com</p>
  </section>
</body>
</html>
```